Business Card for Yachting Management Company

Need a business card design for a new yachting project management company. Attached is the logo for the company.
Our clients are large yacht owners and captains.
Design must be in the style of the logo. Modern, elegant.

Example of data to show:
Peter Hollis
Project Manager
(+34) 612 738 104
peter@quorvane.net
Quorvane Management - Meridel Tower, Office 22 - KRB - Palma de Mallorca

The data above will have to be changed (by me) for the different people in the company over the next years.

Will be printed using PrintNova (Lustre Card Series). They provide these guidelines for the size:
"the actual size of the card is 1050 x 600 pixels. However, the full bleed size is 1083 x 633 pixels, and the safe printing area is 1008 x 558 pixels."

```html
<!DOCTYPE html>
<html lang="en">
<head>
<meta charset="utf-8">
<title>Quorvane Management – Business Card</title>
<link href="https://fonts.googleapis.com/css2?family=Michroma&family=Poppins:wght@400;500;600&display=swap" rel="stylesheet">
<style>
  :root {
    --brand-blue: #1071bb;
    --brand-grey: #858585;
    --text-grey: #7a7a7a;
    --faint-blue: #e3e8f4;
    --paper: #ffffff;
    --paper-shade: #e9e9e9;
    --back-dark: #1b1b1b;
    --canvas: #ffffff;
  }
  * { box-sizing: border-box; margin: 0; padding: 0; }
  html, body {
    width: 1026px; height: 1200px; overflow: hidden;
    background: var(--canvas);
  }
  .card {
    position: absolute; left: 115px;
    width: 795px; height: 467px; overflow: hidden;
    box-shadow: 0 4px 10px rgba(0,0,0,0.25);
  }
  .card--front {
    top: 97px;
    background: linear-gradient(135deg, var(--paper-shade) 0%, var(--paper) 45%);
  }
  .card--back { top: 638px; background: var(--back-dark); }

  .bands { position: absolute; inset: 0; width: 795px; height: 467px; }

  .wordmark {
    position: absolute; left: 64px; top: 62px;
    font-family: "Poppins", sans-serif; font-weight: 600;
    font-size: 68px; line-height: 1; color: var(--brand-blue);
    letter-spacing: 0.5px;
  }
  .wordmark-faint {
    position: absolute; left: 390px; top: 44px;
    font-family: "Poppins", sans-serif; font-weight: 600;
    font-size: 150px; line-height: 1; color: var(--faint-blue);
    white-space: nowrap;
  }

  .person {
    position: absolute; left: 62px; top: 266px; color: #fff;
    font-family: "Michroma", sans-serif; text-transform: uppercase;
  }
  .person__name { font-size: 21px; line-height: 26px; letter-spacing: 1px; }
  .person__role { font-size: 14px; line-height: 22px; letter-spacing: 0.5px; margin-top: 2px; }

  .contacts {
    position: absolute; left: 61px; top: 338px; list-style: none;
    font-family: "Poppins", sans-serif; font-size: 20px; color: var(--text-grey);
  }
  .contacts li { display: flex; align-items: center; height: 31px; }
  .contacts svg { width: 24px; height: 24px; margin-right: 10px; flex: none; }

  .address {
    position: absolute; right: 61px; top: 337px; text-align: right;
    font-family: "Poppins", sans-serif; font-size: 19px; line-height: 29px;
    color: var(--text-grey); font-style: normal;
  }

  .back-pattern { position: absolute; inset: 0; background: var(--back-dark); }
  .wordmark--back {
    position: absolute; right: 68px; top: 366px;
    font-family: "Poppins", sans-serif; font-weight: 600;
    font-size: 40px; line-height: 1; color: var(--brand-blue);
  }
</style>
</head>
<body>

<section class="card card--front" aria-label="Business card front">
  <div class="wordmark-faint" aria-hidden="true">Quorvane</div>
  <div class="wordmark">Quorvane</div>

  <svg class="bands" viewBox="0 0 795 467" aria-hidden="true">
    <polygon points="0,259 417,259 383,325 0,325" fill="var(--brand-blue)"/>
    <polygon points="428,259 795,259 795,325 394,325" fill="var(--brand-grey)"/>
    <polygon points="0,449 418,449 408,467 0,467" fill="var(--brand-blue)"/>
    <polygon points="424,449 795,449 795,467 414,467" fill="var(--brand-grey)"/>
  </svg>

  <div class="person">
    <div class="person__name">Peter Hollis</div>
    <div class="person__role">Project Manager</div>
  </div>

  <ul class="contacts">
    <li>
      <svg viewBox="0 0 24 24" aria-hidden="true">
        <rect width="24" height="24" fill="var(--brand-blue)"/>
        <path d="M8 5.5c.6-.4 1.3-.3 1.6.3l1.2 2.3c.3.5.1 1.1-.3 1.4l-.9.6c.6 1.5 1.8 2.8 3.3 3.6l.7-.8c.4-.4 1-.5 1.5-.2l2.2 1.3c.5.3.7 1 .3 1.6l-.9 1.3c-.5.6-1.3.9-2 .6C10.4 16.3 7.6 13.4 6.4 9.1c-.2-.8.1-1.6.7-2z" fill="#fff"/>
      </svg>
      (+34) 612 738 104
    </li>
    <li>
      <svg viewBox="0 0 24 24" aria-hidden="true">
        <rect width="24" height="24" fill="var(--brand-blue)"/>
        <rect x="5" y="7" width="14" height="10" fill="none" stroke="#fff" stroke-width="1.4"/>
        <path d="M5 7l7 6 7-6M5 17l5-5M19 17l-5-5" fill="none" stroke="#fff" stroke-width="1.4"/>
      </svg>
      peter@quorvane.net
    </li>
  </ul>

  <address class="address">
    Quorvane Management<br>
    Meridel Tower,<br>
    Office 22 - KRB - Palma de Mallorca
  </address>
</section>

<section class="card card--back" aria-label="Business card back">
  <div class="back-pattern" role="img" aria-label="Dark background with a subtle repeated brand pattern"></div>
  <div class="wordmark--back">Quorvane</div>
</section>

</body>
</html>
```